Elegant and Professional Business card design needed

The patron journey mentor is a company which provides consulting services to businesses to assist them in improving the customer experience for their customers.

I need a business card design which tells people I'm there to help them.

Target Market(s)

Small to medium business owners

Industry/Entity Type

Business

Contact Information for Business Card

Martin Glenholme
The Patron Journey Mentor
Web: http://www.ThePatronJourneyMentor.example
Email: martin@ThePatronJourneyMentor.example
Phone: +61 400 582316

Logo styles of interest
Abstract Logo
Requirements
Must have
• Some sort of image / graphic representing the customer is important and should be at the heart of a business.

```html
<!DOCTYPE html>
<html lang="en">
<head>
<meta charset="utf-8">
<title>The Patron Journey Mentor — Business Card</title>
<link rel="stylesheet" href="https://fonts.googleapis.com/css2?family=Fira+Sans+Extra+Condensed:wght@600&family=Source+Sans+3:wght@300;600;700&display=swap">
<style>
  :root {
    --card-bg: #f9ecce;
    --gold: #d4a245;
    --brown: #574a3d;
    --badge: #f0d09b;
  }
  * { margin: 0; padding: 0; box-sizing: border-box; }
  html, body {
    width: 1200px;
    height: 694px;
    overflow: hidden;
    background: var(--card-bg);
  }
  .card {
    position: relative;
    width: 1200px;
    height: 694px;
    background: var(--card-bg);
    font-family: "Source Sans 3", Arial, sans-serif;
  }
  .brand-mark {
    position: absolute;
    left: 283px;
    top: 62px;
  }
  .brand-name {
    position: absolute;
    left: 160px;
    top: 258px;
    font-size: 57px;
    font-weight: 600;
    line-height: 1;
    color: var(--gold);
    letter-spacing: 0.2px;
    white-space: nowrap;
  }
  .person-name {
    position: absolute;
    left: 368px;
    top: 362px;
    font-family: "Fira Sans Extra Condensed", "Arial Narrow", sans-serif;
    font-size: 43px;
    font-weight: 600;
    line-height: 1;
    color: var(--brown);
    white-space: nowrap;
  }
  .contact-list {
    position: absolute;
    left: 355px;
    top: 442px;
    list-style: none;
  }
  .contact-item {
    display: flex;
    align-items: center;
    height: 58px;
    margin-bottom: 14px;
  }
  .contact-badge {
    width: 58px;
    height: 58px;
    border-radius: 50%;
    background: var(--badge);
    color: var(--brown);
    font-weight: 700;
    font-size: 32px;
    line-height: 54px;
    text-align: center;
    flex: none;
  }
  .contact-text {
    margin-left: 21px;
    font-size: 37px;
    font-weight: 300;
    color: var(--brown);
    white-space: nowrap;
  }
</style>
</head>
<body>
  <main class="card">
    <svg class="brand-mark" width="96" height="96" viewBox="0 0 96 96" aria-hidden="true">
      <circle cx="48" cy="48" r="44" fill="var(--gold)"/>
    </svg>
    <h1 class="brand-name">The Patron Journey Mentor</h1>
    <p class="person-name">Martin Glenholme</p>
    <ul class="contact-list">
      <li class="contact-item">
        <span class="contact-badge">w</span>
        <span class="contact-text">www.ThePatronJourneyMentor.example</span>
      </li>
      <li class="contact-item">
        <span class="contact-badge">e</span>
        <span class="contact-text">martin@ThePatronJourneyMentor.example</span>
      </li>
      <li class="contact-item">
        <span class="contact-badge">p</span>
        <span class="contact-text">+61 400 582316</span>
      </li>
    </ul>
  </main>
</body>
</html>
```